strength and conditioning business focused on helping people move more efficiently

I need a business card designed for a Philadelphia based company called Brk Stn Motion (pronounced Brick Stone). We offer fitness professional services with the idea of helping people feel better and move optimally. We do this by designing and walking through individualized programs as well as minor soft tissue work. Our perfect client would be athletes but we will be marketing to parents who have children that are active They remember their former athletic days and want to get as close as possible back to that feeling. Attached will be the official logo and logo formats. I would love for the design to communicate trustworthy and creative. I would also love for the design to be square with rounded edges.

Target Market(s)

Parents of athletic children
former athletes
athletes

Industry/Entity Type

Fitness

Contact Information for Business Card

Business: Brk Stn Athletics
Name: Coach Gareth Milford
Position: Strength and Conditioning Coach / Certified Personal Trainer
Contact: coach.mil@brkstn.example
Text: (555)204-7719

Font styles to use
Serif
Sans Serif

Colors
fbee38
fbee3e
0255a3
3176b5
ffffff

Requirements
Must have
• use of logo
Nice to have
• Square design
rounded edges

```html
<!DOCTYPE html>
<html lang="en">
<head>
<meta charset="utf-8">
<title>Brk Stn Motion – Business Card</title>
<link rel="stylesheet" href="https://fonts.googleapis.com/css2?family=Poppins:wght@400;500;800;900&display=swap">
<style>
  :root {
    --navy: #283d82;
    --navy-soft: #34498f;
    --gold: #f5c518;
    --white: #ffffff;
    --stage: #1c1c1e;
  }
  * { box-sizing: border-box; margin: 0; padding: 0; }
  html, body {
    width: 1200px; height: 900px; overflow: hidden;
    background: var(--stage);
    font-family: "Poppins", sans-serif;
  }
  .canvas {
    position: relative; width: 1200px; height: 900px;
    display: flex; flex-direction: column; align-items: center; justify-content: center; gap: 40px;
  }
  .card {
    width: 700px; height: 400px; border-radius: 6px;
    position: relative; overflow: hidden;
    box-shadow: 0 10px 30px rgba(0,0,0,.5);
  }
  /* front */
  .card-front { background: var(--white); display: flex; align-items: center; }
  .brand-block {
    width: 330px; display: flex; align-items: center; justify-content: center; gap: 14px;
  }
  .brand-dot { width: 26px; height: 26px; border-radius: 50%; background: var(--gold); flex: none; }
  .brand-name {
    color: var(--navy); font-weight: 900; font-size: 50px; line-height: 1; letter-spacing: -1px;
    width: 200px;
  }
  .divider { width: 1.5px; height: 250px; background: var(--navy); }
  .contact-block { padding-left: 36px; color: var(--navy); }
  .coach-name { font-weight: 800; font-size: 21px; text-transform: uppercase; letter-spacing: .3px; }
  .coach-role { font-size: 15px; line-height: 1.35; font-weight: 400; }
  .contact-list { list-style: none; margin-top: 20px; font-size: 15px; }
  .contact-list li { display: flex; align-items: center; gap: 10px; margin-bottom: 6px; }
  .contact-icon { width: 20px; height: 20px; flex: none; }
  /* back */
  .card-back { background: var(--navy); display: flex; align-items: center; justify-content: center; gap: 20px; }
  .card-back .brand-dot { width: 44px; height: 44px; }
  .card-back .brand-name { color: var(--white); width: auto; font-size: 64px; }
</style>
</head>
<body>
<main class="canvas">
  <section class="card card-front">
    <div class="brand-block">
      <span class="brand-dot"></span>
      <span class="brand-name">Brk Stn Motion</span>
    </div>
    <div class="divider"></div>
    <div class="contact-block">
      <h1 class="coach-name">Coach Gareth Milford</h1>
      <p class="coach-role">Strength and Conditioning Coach</p>
      <p class="coach-role">Certified Personal Trainer</p>
      <ul class="contact-list">
        <li>
          <svg class="contact-icon" viewBox="0 0 20 20" aria-hidden="true">
            <circle cx="10" cy="10" r="9" fill="none" stroke="#f5c518" stroke-width="1.6"/>
            <path d="M7 5.5c-.8.6-1.2 1.6-.9 2.8.6 2.3 2.4 4.3 4.6 5.3 1.1.5 2.2.3 2.9-.5l-1.6-1.6-1.2.7c-1-.6-1.8-1.5-2.3-2.5l.8-1.1z" fill="#f5c518"/>
          </svg>
          <span>(555)204-7719</span>
        </li>
        <li>
          <svg class="contact-icon" viewBox="0 0 20 20" aria-hidden="true">
            <circle cx="10" cy="10" r="9" fill="none" stroke="#f5c518" stroke-width="1.6"/>
            <rect x="5.5" y="6.8" width="9" height="6.4" rx=".8" fill="#f5c518"/>
            <path d="M5.8 7.2 10 10.4l4.2-3.2" fill="none" stroke="#ffffff" stroke-width="1"/>
          </svg>
          <span>coach.mil@brkstn.example</span>
        </li>
      </ul>
    </div>
  </section>

  <section class="card card-back">
    <span class="brand-dot"></span>
    <span class="brand-name">Brk Stn Motion</span>
  </section>
</main>
</body>
</html>
```